Lomi-Seret - Promote and Support a community

Design a website for Ethiopean Community. the design should be friendly, easy to navigate and maintain the look & feel of the Ethiopian culture. a proposed logo is attached but it can be change according to your recommendations. This is a project we are doing at a discount rate as it supports a weak community.
Please visit their current website http://www.lomi-seret.example.il/index.php?lang=en

Target Market(s)

Community members, potential doners

Industry/Entity Type

community

Number of Pages Required

1 page

Font styles to use
Sans Serif

Requirements
Must have
• easy to navigate friendly interface

```html
<!DOCTYPE html>
<html lang="en">
<head>
<meta charset="utf-8">
<title>Lomi Seret – Ethiopean Community</title>
<link href="https://fonts.googleapis.com/css2?family=Play:wght@400;700&family=Poppins:wght@400;500;600&display=swap" rel="stylesheet">
<style>
:root{
  --red:#d2161c;
  --red-deep:#8e0c12;
  --maroon:#2a0407;
  --green:#1d7a4b;
  --green-soft:#e5f0eb;
  --yellow:#e4bf26;
  --gold:#e0a821;
  --ink:#3b3b3b;
  --muted:#666;
  --grey-bg:#f0f3f2;
  --frame:#e3e9e7;
  --white:#fff;
}
*{box-sizing:border-box;margin:0;padding:0}
html,body{width:1200px;height:4894px;overflow:hidden;background:var(--white)}
body{font-family:"Poppins",sans-serif;color:var(--ink)}
.page{position:relative;width:1200px;height:4894px;overflow:hidden}
.abs{position:absolute}
.heading{font-family:"Play",sans-serif;font-weight:700;color:var(--red-deep)}
.photo{position:absolute;border-radius:6px;overflow:hidden}
.btn{position:absolute;display:flex;align-items:center;justify-content:center;background:var(--red);color:var(--white);font-size:13px;font-weight:500;border-radius:20px;letter-spacing:.3px}
.btn.inline{position:relative}
.body-text{font-size:11px;line-height:19px;color:var(--muted)}
.eyebrow{font-size:12px;color:var(--gold);display:flex;align-items:center;gap:10px}
.eyebrow::after{content:"";width:34px;height:2px;background:var(--gold)}

/* text blocks in normal flow */
.text-block{position:absolute}
.text-block .body-text{margin-bottom:12px}
.text-block .btn{margin-top:8px}

/* nav */
.nav{position:absolute;top:0;left:0;width:1200px;height:60px;background:var(--white);z-index:3}
.nav a{position:absolute;top:23px;font-size:11.5px;color:var(--ink);text-decoration:none}
.nav .active{top:15px;left:184px;width:67px;height:31px;background:var(--red);color:#fff;border-radius:16px;display:flex;align-items:center;justify-content:center}
.lang{position:absolute;left:1071px;top:14px;width:69px;height:31px;border:1.5px solid var(--red);border-radius:16px;color:var(--red);font-size:12px;display:flex;align-items:center;justify-content:center;gap:6px}
.brand-badge{position:absolute;left:546px;top:6px;width:108px;height:108px;border-radius:50%;background:var(--white);border:3px solid var(--red);z-index:4;display:flex;align-items:center;justify-content:center;font-weight:600;font-size:14px;color:var(--red)}

/* hero */
.hero-circle{position:absolute;left:703px;top:105px;width:436px;height:436px;border-radius:50%;background:rgba(29,122,75,.92);z-index:2;text-align:center;color:#fff;padding-top:118px}
.hero-circle h1{font-family:"Play",sans-serif;font-size:38px;line-height:46px;font-weight:700;white-space:nowrap}
.hero-circle h1 span{display:block;color:var(--yellow)}
.hero-circle p{font-size:11.5px;line-height:21px;width:380px;margin:12px auto 0}

/* stats */
.stat{position:absolute;top:1216px;width:240px;text-align:center}
.stat-ring{width:116px;height:116px;margin:0 auto;border-radius:50%;display:flex;align-items:center;justify-content:center}
.stat-core{width:94px;height:94px;border-radius:50%;display:flex;align-items:center;justify-content:center}
.stat-num{font-size:23px;font-weight:500;margin-top:16px}
.stat-label{font-size:12.5px;line-height:19px;color:var(--ink);margin-top:6px}

/* program */
.program-card{position:absolute;width:256px;height:262px;overflow:hidden;border-radius:2px}
.program-card span{position:absolute;left:22px;bottom:16px;font-family:"Play",sans-serif;font-size:16px;line-height:20px;color:#fff;font-weight:700}

/* partners */
.partner{position:absolute;width:170px;height:80px;display:flex;align-items:center;justify-content:center}
.partner i{display:block;background:#d9dfe3;border-radius:6px}

/* news */
.news-card{position:absolute;top:4066px;width:378px}
.news-img{position:relative;height:224px;border-radius:6px;overflow:hidden}
.news-date{position:absolute;left:12px;bottom:8px;background:var(--gold);color:#fff;font-size:12px;padding:4px 12px}
.news-card h3{font-family:"Play",sans-serif;font-size:19px;color:var(--ink);font-weight:400;margin:26px 0 10px -4px}
.news-card a{font-size:11.5px;color:var(--red);text-decoration:underline;display:block;margin-top:12px}

/* footer */
.contact{position:absolute;top:4716px;display:flex;align-items:center;gap:14px}
.contact .ico{width:38px;height:38px;border-radius:50%;background:var(--red);display:flex;align-items:center;justify-content:center}
.contact small{display:block;font-size:10.5px;color:var(--red)}
.contact b{display:block;font-size:12px;font-weight:400;color:#fff}
.foot-links{position:absolute;top:4796px;width:1200px;text-align:center;font-size:10.5px;color:#fff}
.copy{position:absolute;top:4826px;width:1200px;text-align:center;font-size:10.5px;color:#ddd}
</style>
</head>
<body>
<div class="page">

<!-- NAVIGATION -->
<nav class="nav">
  <a class="active" href="#">Home</a>
  <a href="#" style="left:265px">About</a>
  <a href="#" style="left:318px">The Community</a>
  <a href="#" style="left:428px">Programs</a>
  <a href="#" style="left:502px">News</a>
  <a href="#" style="left:674px">Advocacy</a>
  <a href="#" style="left:750px">Partners</a>
  <a href="#" style="left:817px">Supports Us</a>
  <a href="#" style="left:906px">Contact Us</a>
  <div class="lang">
    <svg width="13" height="13" viewBox="0 0 14 14" fill="none" stroke="currentColor" stroke-width="1.2"><circle cx="7" cy="7" r="6"/><ellipse cx="7" cy="7" rx="2.6" ry="6"/><path d="M1 7h12"/></svg>EN
  </div>
</nav>
<div class="brand-badge">Lomi Seret</div>

<!-- HERO -->
<svg class="abs" style="left:0;top:60px" width="1200" height="660" viewBox="0 60 1200 660" role="img" aria-label="Ethiopian immigrants in white traditional dress waving Israeli flags on a red carpet at the airport">
  <defs>
    <linearGradient id="heroFill" x1="0" y1="0" x2="0" y2="1">
      <stop offset="0" stop-color="#8b8f93"/>
      <stop offset=".55" stop-color="#6e6a68"/>
      <stop offset=".8" stop-color="#b3262b"/>
      <stop offset="1" stop-color="#c9282c"/>
    </linearGradient>
  </defs>
  <path d="M0 60H1200V437Q600 990 0 437Z" fill="url(#heroFill)"/>
  <path d="M0 437Q600 990 1200 437" fill="none" stroke="var(--yellow)" stroke-width="5"/>
</svg>
<div class="hero-circle">
  <h1>Lomi Seret<span>Ethiopean Community</span></h1>
  <p>Aliyah (immigration) from Ethiopia to Israel and the transition to a sedentary lifestyle has resulted in the emergence of chronic diseases, in particular diabetes</p>
  <div class="btn inline" style="width:140px;height:38px;margin:16px auto 0">CONTACT US</div>
</div>

<!-- ABOUT -->
<div class="photo" style="left:160px;top:762px;width:134px;height:135px;background:linear-gradient(135deg,#8aa6b8,#c9b79a);z-index:1" role="img" aria-label="Community elders seated outdoors"></div>
<div class="photo" style="left:200px;top:808px;width:262px;height:285px;background:linear-gradient(160deg,#d32a22 0%,#e3b52a 35%,#2f7d3c 60%,#2a3f7a 85%)" role="img" aria-label="Young people celebrating with Ethiopian and American flags"></div>
<div class="photo" style="left:392px;top:1005px;width:136px;height:135px;background:linear-gradient(135deg,#e8e4e0,#b72a2a);box-shadow:0 0 0 4px #fff" role="img" aria-label="Children at a health activity"></div>

<div class="text-block" style="left:632px;top:797px;width:400px">
  <div class="eyebrow">Welcome To</div>
  <h2 class="heading" style="font-size:32px;margin:4px 0 12px -2px">Lomi Seret</h2>
  <p class="body-text">Aliyah (immigration) from Ethiopia to Israel and the transition to a sedentary lifestyle has resulted in the emergence of chronic diseases, in particular diabetes.</p>
  <p class="body-text">While only 0.4% of the new immigrants were diagnosed with Type 2 diabetes upon arrival, by the time they had lived in Israel for ten years the figure had risen to 18% - three times as many as in the general population. The incidence of hypertension, obesity, asthma and Type 1 diabetes had also increased dramatically.</p>
  <p class="body-text">Lomi Seret was founded in 1999 by Dr. Miriam Adler, Head of the Endocrinology Unit at the Carmel Valley Medical Center.</p>
  <div class="btn inline" style="width:137px;height:40px">LEARN MORE</div>
</div>

<!-- STATS -->
<div class="stat" style="left:224px">
  <div class="stat-ring" style="border:1.5px solid var(--green);border-bottom-color:transparent;border-left-color:transparent"><div class="stat-core" style="background:var(--green-soft)">
    <svg width="40" height="40" viewBox="0 0 40 40" fill="none" stroke="var(--green)" stroke-width="2"><rect x="16" y="12" width="16" height="20" rx="2"/><path d="M8 6v10a6 6 0 0 0 12 0V6M14 22v8a5 5 0 0 0 5 5"/><path d="M20 18h8M20 23h8M20 28h5"/></svg>
  </div></div>
  <div class="stat-num" style="color:var(--green)">0.4%</div>
  <div class="stat-label">Of the New Immigrants Were Diagnosed</div>
</div>
<div class="stat" style="left:480px">
  <div class="stat-ring" style="border:1.5px solid var(--yellow);border-bottom-color:transparent;border-left-color:transparent"><div class="stat-core" style="background:#fbf4dc">
    <svg width="40" height="40" viewBox="0 0 40 40" fill="none" stroke="var(--gold)" stroke-width="2"><rect x="6" y="10" width="20" height="14" rx="2"/><path d="M10 15h12M10 19h8"/><path d="M30 20c-3 5-5 7-5 10a5 5 0 0 0 10 0c0-3-2-5-5-10z"/></svg>
  </div></div>
  <div class="stat-num" style="color:var(--gold)">2</div>
  <div class="stat-label">Diabetes Upon Arrival, by the time they had Lived in Israel for ten Years the Figure had Risen</div>
</div>
<div class="stat" style="left:737px">
  <div class="stat-ring" style="border:1.5px solid var(--red);border-bottom-color:transparent;border-left-color:transparent"><div class="stat-core" style="background:#fbe6e6">
    <svg width="40" height="40" viewBox="0 0 40 40" fill="none" stroke="var(--red)" stroke-width="2"><circle cx="12" cy="14" r="4"/><circle cx="20" cy="11" r="4"/><circle cx="28" cy="14" r="4"/><path d="M5 32v-6a7 7 0 0 1 14 0v6M13 32v-8a7 7 0 0 1 14 0v8M21 32v-6a7 7 0 0 1 14 0v6"/></svg>
  </div></div>
  <div class="stat-num" style="color:var(--red)">18%</div>
  <div class="stat-label">Three Times as many as in the General Population</div>
</div>

<!-- PROGRAM -->
<svg class="abs" style="left:0;top:1530px" width="1200" height="1160" viewBox="0 1530 1200 1160">
  <defs>
    <linearGradient id="programBand" x1="0" y1="0" x2="1" y2="0">
      <stop offset="0" stop-color="#1f7f4e"/>
      <stop offset=".5" stop-color="#7fa53a"/>
      <stop offset="1" stop-color="#e7c42a"/>
    </linearGradient>
  </defs>
  <path d="M0 1955Q600 2180 1200 1955V2680H0Z" fill="url(#programBand)"/>
  <path d="M170 1630V1542H1031V1630" fill="none" stroke="var(--frame)" stroke-width="7"/>
</svg>
<div class="eyebrow abs" style="left:502px;top:1620px">What We Do</div>
<h2 class="heading abs" style="left:0;width:1200px;text-align:center;top:1640px;font-size:32px">Our Program</h2>

<div class="program-card" style="left:190px;top:1771px;background:linear-gradient(160deg,#c98a2a,#4a3a30)" role="img" aria-label="Health education presentation to a seated group"><span>Health Education<br>Presentations</span></div>
<div class="program-card" style="left:469px;top:1714px;background:linear-gradient(160deg,#c9c9c4,#3d4140)" role="img" aria-label="Doctors at a regional health fair"><span>Regional Health<br>Fairs</span></div>
<div class="program-card" style="left:752px;top:1771px;background:linear-gradient(160deg,#b8c6d3,#5a3f3a)" role="img" aria-label="Woman speaking into a radio microphone"><span>Amharic Radio<br>Program</span></div>
<div class="program-card" style="left:190px;top:2056px;background:linear-gradient(160deg,#e5e1dc,#3a2f2a)" role="img" aria-label="Health leaders in white coats"><span>Health Leadership<br>Development</span></div>
<div class="program-card" style="left:469px;top:1999px;background:linear-gradient(160deg,#9c7d5e,#4d3a2c)" role="img" aria-label="Table of prepared food at a cookery course"><span>Nutrition &amp; Cokkery<br>Courses</span></div>
<div class="program-card" style="left:752px;top:2056px;background:linear-gradient(160deg,#d6e0e2,#2d6a5a)" role="img" aria-label="Healthcare personnel training with a patient"><span>Healthcare Personnel<br>Tranning</span></div>
<div class="abs" style="left:0;width:1200px;text-align:center;top:2290px;font-size:12px;color:var(--green);text-decoration:underline;font-weight:500">Explore More</div>

<h2 class="abs" style="left:0;width:1200px;text-align:center;top:2412px;font-family:'Play',sans-serif;font-size:32px;color:#fff;font-weight:400">Lomi Seret</h2>
<p class="abs" style="left:0;width:1200px;text-align:center;top:2474px;font-size:17px;line-height:28px;color:#fff">Lomi means health in Amharic, and also signifies a jewel<br>basket: an expensive and unique gift to preserve.</p>
<p class="abs" style="left:0;width:1200px;text-align:center;top:2554px;font-size:17px;line-height:32px;color:#fff">Seret Means Health In Hebrew.<br>Health Is a Gift To Be Preserved.</p>

<!-- COMMUNITY -->
<div class="abs" style="left:0;top:2681px;width:600px;height:427px;background:var(--grey-bg)"></div>
<div class="abs" style="left:600px;top:2681px;width:600px;height:427px;background:linear-gradient(160deg,#6a6a60 0%,#b23a36 45%,#d4242a 75%,#4f6a3a 100%)" role="img" aria-label="Crowd of community members and first-aid volunteers in red vests sitting on the grass"></div>
<div class="text-block" style="left:61px;top:2752px;width:440px">
  <h2 class="heading" style="font-size:33px;margin-left:-1px">The Community</h2>
  <div class="eyebrow" style="margin:4px 0 14px">Health &amp; the Ethiopian Israeli Community</div>
  <p class="body-text" style="font-size:10.5px;line-height:18px">Today the Ethiopian Israeli community numbers over 120,000 with new immigrants still continuing to arrive. For many, immigration led to the disintegration of traditional family and social structures with traumatic results for the community and further impeding absorption into Israeli society.</p>
  <p class="body-text" style="font-size:10.5px;line-height:18px">"Ethiopian immigrants ranked lowest on the quality of life index, which considers per-capita income, per-room housing density &amp; basic spending"</p>
  <div class="btn inline" style="width:135px;height:40px;margin-top:4px">LEARN MORE</div>
</div>

<!-- SUPPORT -->
<h2 class="heading abs" style="left:508px;top:3178px;font-size:33px">Support Us</h2>
<div class="abs" style="left:702px;top:3201px;width:32px;height:2px;background:var(--gold)"></div>
<svg class="abs" style="left:0;top:3250px" width="1200" height="200">
  <g stroke="#e6e6e6" stroke-width="1">
    <path d="M429 32V120M600 32V120M771 32V120"/>
    <path d="M258 122H942"/>
    <path d="M514 124V210M686 124V210"/>
  </g>
</svg>
<div class="partner" style="left:259px;top:3252px"><i style="width:100px;height:36px"></i></div>
<div class="partner" style="left:430px;top:3252px"><i style="width:110px;height:22px"></i></div>
<div class="partner" style="left:601px;top:3252px"><i style="width:40px;height:48px"></i></div>
<div class="partner" style="left:772px;top:3252px"><i style="width:120px;height:28px"></i></div>
<div class="partner" style="left:344px;top:3346px"><i style="width:76px;height:50px"></i></div>
<div class="partner" style="left:515px;top:3346px"><i style="width:120px;height:26px"></i></div>
<div class="partner" style="left:686px;top:3346px"><i style="width:60px;height:48px"></i></div>

<!-- NEWSLETTER + NEWS -->
<svg class="abs" style="left:0;top:3500px" width="1200" height="840" viewBox="0 3500 1200 840">
  <defs>
    <radialGradient id="redBand" cx=".5" cy=".35" r=".7">
      <stop offset="0" stop-color="#d8262a"/>
      <stop offset="1" stop-color="#a80f16"/>
    </radialGradient>
  </defs>
  <rect x="0" y="3502" width="1200" height="830" fill="url(#redBand)"/>
  <path d="M0 4095C300 3890 900 3890 1200 4300V4340H0Z" fill="#fff"/>
</svg>
<div class="abs" style="left:114px;top:3552px;width:456px;height:420px;border-radius:48% 48% 0 0;background:linear-gradient(180deg,#e9e4dc 0%,#b56b4a 60%,#c8413a 100%)" role="img" aria-label="Mother in a white shawl holding her young child"></div>
<h2 class="abs" style="left:604px;width:430px;text-align:center;top:3572px;font-family:'Play',sans-serif;font-size:33px;color:#fff;font-weight:400">Newsletter Signup !</h2>
<p class="abs" style="left:594px;width:450px;text-align:center;top:3630px;font-size:12px;line-height:21px;color:#fff">We are pleased to announce that "LOMI SERET" was awarded the prize of the Ministry of Health for excellence in volunteer activity.</p>
<div class="abs" style="left:604px;top:3691px;width:427px;height:37px;border-radius:19px;background:#fff;font-size:11px;color:#777;padding:11px 20px">Enter Name*</div>
<div class="abs" style="left:604px;top:3743px;width:427px;height:37px;border-radius:19px;background:#fff;font-size:11px;color:#777;padding:11px 20px">Enter Email*</div>
<div class="btn" style="left:756px;top:3798px;width:127px;height:36px;background:#c3080e">SUBSCRIBE</div>

<h2 class="heading abs" style="left:498px;top:3984px;font-size:33px">Latest News</h2>
<div class="abs" style="left:712px;top:4007px;width:32px;height:2px;background:var(--gold)"></div>

<div class="news-card" style="left:211px">
  <div class="news-img" style="background:linear-gradient(160deg,#7d9a5a,#6a5a48)" role="img" aria-label="Villagers gathered on a dirt road beside a vehicle">
    <span class="news-date">March 2002</span>
  </div>
  <h3>“Health Matters”</h3>
  <p class="body-text">Lorem Ipsum has been the industry's standard dummy text ever since thes, when an unknown printer...</p>
  <a href="#">Read More</a>
</div>
<div class="news-card" style="left:614px">
  <div class="news-img" style="background:linear-gradient(160deg,#9c8a7a,#2f2a28)" role="img" aria-label="Mother and children speaking at a community event">
    <span class="news-date">March 2002</span>
  </div>
  <h3>“Health Matters”</h3>
  <p class="body-text">Lorem Ipsum has been the industry's standard dummy text ever since thes, when an unknown printer...</p>
  <a href="#">Read More</a>
</div>

<!-- FOOTER -->
<svg class="abs" style="left:0;top:4500px" width="1200" height="394" viewBox="0 4500 1200 394">
  <path d="M0 4650Q600 4400 1200 4650V4894H0Z" fill="var(--maroon)"/>
</svg>
<div class="abs" style="left:546px;top:4554px;width:108px;height:108px;border-radius:50%;background:var(--maroon);border:2px solid var(--red);display:flex;align-items:center;justify-content:center;font-weight:600;font-size:14px;color:var(--red)">Lomi Seret</div>

<div class="contact" style="left:218px">
  <div class="ico"><svg width="18" height="18" viewBox="0 0 24 24" fill="#fff"><path d="M6.6 10.8a15 15 0 0 0 6.6 6.6l2.2-2.2a1 1 0 0 1 1-.25 11.4 11.4 0 0 0 3.6.57 1 1 0 0 1 1 1V20a1 1 0 0 1-1 1A17 17 0 0 1 3 4a1 1 0 0 1 1-1h3.5a1 1 0 0 1 1 1c0 1.25.2 2.45.57 3.57a1 1 0 0 1-.25 1z"/></svg></div>
  <div><small>Phone</small><b>04 - 555 - 0187</b></div>
</div>
<div class="contact" style="left:456px">
  <div class="ico"><svg width="16" height="18" viewBox="0 0 24 24" fill="#fff"><path d="M12 2a7 7 0 0 0-7 7c0 5 7 13 7 13s7-8 7-13a7 7 0 0 0-7-7zm0 9.5A2.5 2.5 0 1 1 12 6.5a2.5 2.5 0 0 1 0 5z"/></svg></div>
  <div><small>Office</small><b>Rimon 12/4 POB 4120 Netanya, 42150</b></div>
</div>
<div class="contact" style="left:801px">
  <div class="ico"><svg width="18" height="16" viewBox="0 0 24 20" fill="#fff"><path d="M2 2h20v16H2zm2 2v.5l8 5.5 8-5.5V4zm0 3v9h16V7l-8 5.5z"/></svg></div>
  <div><small>Email</small><b>lomiseret@example.org</b></div>
</div>

<div class="foot-links">Home &nbsp;|&nbsp; About &nbsp;|&nbsp; The Community &nbsp;|&nbsp; Programs &nbsp;|&nbsp; News &nbsp;|&nbsp; Advocacy &nbsp;|&nbsp; Partners &nbsp;|&nbsp; Support Us &nbsp;|&nbsp; Contact Us</div>
<div class="copy">©Lomi Seret - 2022 All rights reserved.</div>

</div>
</body>
</html>
```